Info about Getting Rid of Items That People No Longer Want or Need and Would Rather Have the Cash

We need a flyer made to pass out to potential customers describing what it is that we do. We would like for it to be a one page front and back flyer.
Our company helps people who are downsizing or getting rid of items that they no longer want and are unsure of their value. Most Millennials have no interest in their parents items--whether that be art, sterling flatware, jewelry, decorative items or collectibles. On top of that the market is slowing turning as there is more 'stuff" on the market than ever before and less buyers.
We have included some images as examples. For instance: a newspaper headline showing "Millennials Don't Want Your Stuff". In one of the small columns below there could be a picture of an Bruno Kessick painting with a caption reading "Man Buys Original Kessick for $20 in Garage Sale". Or something like that.
We are open to suggestions and encourage your creativity. These are just examples of what we came up with. These issues, kids not wanting their parents stuff and worry about squandering something special because they didn't know what it is and what its worth are big concerns.
On the back page we are thinking about using a 5 step process to simplify what we do.
Below is a rough example of the 5 steps.
1) Schedule Free In-Home Visit
Please contact us to schedule an appointment
2) Questions, Answers and Facts
We will answer any questions you have and ask you enough questions to make sure we know what your goals are. We will also inform you about market trends and other information related to downsizing
3) The Tour and The Treasure Hunt
You will take us on a tour of your home and point out items you are selling. We will take pictures, notes and point out any treasures that you may not realize you have.
4) Research, Research, Research
We take our notes and photographs back to research your items. Then we will check with our network of experts, dealers and buyers across the country to determine the best market.
5) The Game Plan
We will go over our findings with you. Then we will discuss ways to sell the items to get the highest return.
We have also attached sample images of our business card. We will also want to include our contact information:
Walter Brannock
555-382-7190
info@walterbbrannock-example.com
www.walterbbrannock-example.com
Target Market(s)
Elderly People or people downsizing
Industry/Entity Type
Cash
Font styles to use
Colors
Designer to choose colors to be used in the design.
Look and feel
Each slider illustrates characteristics of the customer's brand and the style your logo design should communicate.

```html
<!DOCTYPE html>
<html lang="en">
<head>
<meta charset="utf-8">
<title>Walter B Brannock – Collectible Asset Flyer</title>
<link rel="stylesheet" href="https://fonts.googleapis.com/css2?family=Oswald:wght@400;500;600&family=Roboto+Condensed:wght@400;700&family=Roboto:wght@400;500&display=swap">
<style>
  :root {
    --backdrop: #c9c8c8;
    --label: #2a1f1a;
    --wood-dark: #1f120c;
    --wood-mid: #3a2317;
    --wood-light: #4a2e1e;
    --gold: #a57a3a;
    --gold-light: #c19a5b;
    --white: #ffffff;
    --ink: #f1e9df;
  }
  * { box-sizing: border-box; margin: 0; padding: 0; }
  html, body { width: 1200px; height: 1200px; overflow: hidden; }
  body { background: var(--backdrop); position: relative; font-family: "Roboto", Arial, sans-serif; }

  .side-label {
    position: absolute; top: 166px; width: 540px; text-align: center;
    font-family: "Roboto Condensed", Arial, sans-serif; font-weight: 700;
    font-size: 40px; color: var(--label); letter-spacing: 1px;
  }
  .side-label.front { left: 30px; }
  .side-label.back { left: 600px; }

  .page {
    position: absolute; top: 253px; width: 540px; height: 694px; overflow: hidden;
    background: linear-gradient(100deg, var(--wood-dark) 0%, var(--wood-mid) 35%, var(--wood-light) 55%, var(--wood-mid) 80%, var(--wood-dark) 100%);
    box-shadow: 3px 4px 8px rgba(0,0,0,0.35);
    color: var(--ink);
  }
  .page.front { left: 45px; }
  .page.back { left: 617px; }
  .abs { position: absolute; }

  /* Front */
  .hero-photo {
    left: 0; top: 0; width: 540px; height: 279px;
    background: radial-gradient(ellipse at 35% 45%, #6b4a2e 0%, #4a2f1c 45%, #2a1810 100%);
  }
  .hero-band { left: 0; top: 279px; width: 540px; height: 8px; background: var(--gold); }
  .hero-name {
    left: 190px; top: 100px; width: 320px; text-align: center;
    font-family: "Oswald", sans-serif; font-weight: 500; font-size: 38px; line-height: 1;
    color: var(--white); text-shadow: 1px 2px 3px rgba(0,0,0,0.6);
  }
  .hero-role {
    left: 190px; top: 145px; width: 320px; text-align: center;
    font-family: "Roboto Condensed", sans-serif; font-size: 11.5px; color: var(--white);
  }
  .headline {
    left: 0; top: 314px; width: 540px; text-align: center;
    font-family: "Oswald", sans-serif; font-weight: 500; font-size: 28px; color: var(--white); letter-spacing: 0.3px;
  }
  .brush-banner { left: 41px; top: 405px; width: 290px; height: 86px; }
  .banner-text {
    left: 41px; top: 421px; width: 290px; text-align: center;
    font-family: "Oswald", sans-serif; font-weight: 500; font-size: 15.5px; line-height: 1.25; color: var(--gold);
  }
  .banner-text strong { color: #2a1a10; font-weight: 600; }
  .painting {
    left: 373px; top: 373px; width: 124px; height: 124px;
    background: radial-gradient(circle at 50% 50%, #f0a0b0 0%, #f2d23a 45%, #3cb8b0 75%);
  }
  .painting-caption {
    left: 365px; top: 502px; width: 140px; text-align: center;
    font-family: "Oswald", sans-serif; font-weight: 500; font-size: 15px; line-height: 1.1; color: var(--white);
  }
  .painting-caption span { display: block; font-family: "Roboto Condensed", sans-serif; font-weight: 400; font-size: 10px; color: #d8cfc4; }

  .bio-box {
    left: 20px; top: 561px; width: 484px; height: 84px;
    border: 1.5px solid var(--white); border-radius: 5px;
    padding: 17px 8px 0 8px;
    font-family: "Roboto", sans-serif; font-size: 8.2px; line-height: 1.22; color: var(--white); text-align: justify;
  }
  .tab {
    position: absolute; background: var(--gold); color: var(--white);
    font-family: "Oswald", sans-serif; font-weight: 500; border-radius: 6px; white-space: nowrap;
    transform: translateX(-50%);
  }
  .bio-tab {
    left: 262px; top: 550px; padding: 0 6px; font-size: 14px; line-height: 20px;
    background: var(--white); color: var(--gold); border: 1.5px solid var(--white);
  }

  .footer {
    left: 0; top: 656px; width: 540px; height: 38px; background: var(--wood-dark); border-top: 2px solid var(--gold);
    display: flex; align-items: center; justify-content: space-between; padding: 0 16px;
  }
  .contact {
    display: flex; align-items: center; gap: 4px;
    font-family: "Roboto", sans-serif; font-size: 8px; color: var(--white); white-space: nowrap;
  }
  .contact svg { width: 8px; height: 8px; flex: none; }

  /* Back */
  .corner-brush { left: 280px; top: 0; width: 260px; height: 66px; }
  .section-title {
    left: 31px; top: 35px; font-family: "Oswald", sans-serif; font-weight: 500; font-size: 15px; color: var(--gold-light);
  }
  .step {
    position: absolute; left: 41px; border: 1.5px solid var(--white); border-radius: 5px;
    padding: 3px 8px 0 24px; color: var(--white);
  }
  .step h3 { font-family: "Roboto", sans-serif; font-weight: 500; font-size: 12px; letter-spacing: 0.2px; margin-bottom: 4px; }
  .step p { font-family: "Roboto", sans-serif; font-size: 8.3px; line-height: 1.25; }
  .step-icon {
    position: absolute; left: -17px; top: 50%; width: 34px; height: 34px; margin-top: -17px;
    border-radius: 50%; background: var(--white); border: 2px solid var(--gold);
    display: flex; align-items: center; justify-content: center;
  }
  .step-icon svg { width: 20px; height: 20px; }
  .s1 { top: 70px; width: 248px; height: 37px; }
  .s2 { top: 128px; width: 474px; height: 49px; }
  .s3 { top: 196px; width: 474px; height: 51px; }
  .s4 { top: 268px; width: 474px; height: 51px; }
  .s5 { top: 334px; width: 444px; height: 41px; }

  .asset-box {
    left: 24px; top: 448px; width: 488px; height: 55px;
    border: 1.5px solid var(--gold); border-radius: 5px; padding: 12px 7px 0 7px;
    font-family: "Roboto", sans-serif; font-size: 8.3px; line-height: 1.25; color: var(--white);
  }
  .asset-tab { left: 270px; top: 437px; padding: 1px 18px; font-size: 13px; }

  .item-photo { position: absolute; top: 542px; width: 78px; height: 84px; background: var(--white); padding: 4px; box-shadow: 2px 2px 4px rgba(0,0,0,0.5); }
  .item-photo div { width: 100%; height: 100%; }
  .i1 { left: 52px; } .i1 div { background: linear-gradient(160deg, #f4f4f4, #9a8ad0 45%, #e4c040 70%, #f4f4f4); }
  .i2 { left: 162px; } .i2 div { background: radial-gradient(circle, #cfc7b4 0%, #6a5a3a 60%, #3a2a1a 100%); }
  .i3 { left: 282px; } .i3 div { background: radial-gradient(circle at 50% 40%, #c8c8c8 0%, #3a3a3a 55%, #111 100%); }
  .i4 { left: 406px; } .i4 div { background: radial-gradient(circle at 50% 55%, #d8d0c4 0%, #a89c8c 45%, #f6f6f6 80%); }
</style>
</head>
<body>
  <div class="side-label front">FRONT</div>
  <div class="side-label back">BACK</div>

  <!-- Front page -->
  <section class="page front">
    <div class="abs hero-photo" role="img" aria-label="Photo of Walter B Brannock in a suit, arms crossed, in front of wooden bookshelves"></div>
    <div class="abs hero-band"></div>
    <h1 class="abs hero-name">WALTER B BRANNOCK</h1>
    <p class="abs hero-role">COLLECTIBLE ASSET BUYER, BROKER &amp; CONSULTANT</p>

    <h2 class="abs headline">MILLENNIALS DON'T WANT YOUR STUFF</h2>

    <svg class="abs brush-banner" viewBox="0 0 290 86" aria-hidden="true">
      <polygon points="12,10 286,4 276,38 290,58 250,80 20,86 0,60 10,38" fill="#ffffff"/>
    </svg>
    <p class="abs banner-text">Man Buys Original Kessick<br>for <strong>$20</strong> in Garage Sale</p>

    <div class="abs painting" role="img" aria-label="Pop-art portrait painting by Bruno Kessick"></div>
    <p class="abs painting-caption">BRUNO KESSICK<span>Painting</span></p>

    <div class="abs bio-box">Over the last 15 years I have been able to help thousands of clients sell their items. During this time I have purchased millions of dollars worth of jewelry, coins, watches, sterling and collectibles. Throughout the years we have maintained an A+ rating with the Regional Trade Standards Council and have never had a complaint. Over 95% of our business comes through referrals from prior customers and companies that serve the estate and senior industry including auction houses, realtors, senior communities and estate sale companies. We are proud of our reputation and work hard to grow our standing in the community.</div>
    <div class="tab bio-tab">WALTER B BRANNOCK</div>

    <footer class="abs footer">
      <span class="contact"><svg viewBox="0 0 10 10"><circle cx="5" cy="5" r="5" fill="#c19a5b"/><circle cx="5" cy="4" r="1.8" fill="#1f120c"/><path d="M2 8.5a3 2.4 0 0 1 6 0z" fill="#1f120c"/></svg>Walter Brannock</span>
      <span class="contact"><svg viewBox="0 0 10 10"><path d="M2 1l2 2-1 1.2a6 6 0 0 0 2.8 2.8L7 6l2 2-1.3 1.3C4.5 9 1 5.5.7 2.3z" fill="#c19a5b"/></svg>555-382-7190</span>
      <span class="contact"><svg viewBox="0 0 10 10"><circle cx="5" cy="5" r="5" fill="#c19a5b"/><rect x="2.2" y="3.2" width="5.6" height="3.8" fill="#1f120c"/><path d="M2.2 3.2L5 5.4 7.8 3.2" stroke="#c19a5b" stroke-width=".6" fill="none"/></svg>info@walterbbrannock-example.com</span>
      <span class="contact"><svg viewBox="0 0 10 10"><circle cx="5" cy="5" r="4.4" fill="none" stroke="#c19a5b" stroke-width="1.2"/><path d="M.6 5h8.8M5 .6c-2.4 2.6-2.4 6.2 0 8.8M5 .6c2.4 2.6 2.4 6.2 0 8.8" stroke="#c19a5b" stroke-width=".7" fill="none"/></svg>www.walterbbrannock-example.com</span>
    </footer>
  </section>

  <!-- Back page -->
  <section class="page back">
    <svg class="abs corner-brush" viewBox="0 0 260 66" aria-hidden="true">
      <polygon points="30,0 260,0 260,8 120,56 96,66 70,48 0,30 20,12" fill="#ffffff"/>
    </svg>
    <h2 class="abs section-title">WHAT WE DO</h2>

    <div class="step s1">
      <span class="step-icon"><svg viewBox="0 0 20 20"><rect x="2" y="4" width="16" height="14" rx="1" fill="none" stroke="#a57a3a" stroke-width="1.5"/><path d="M2 8h16M6 2v4M14 2v4" stroke="#a57a3a" stroke-width="1.5"/></svg></span>
      <h3>SCHEDULE FREE IN-HOME VISIT</h3>
      <p>Please contact us to schedule an appointment</p>
    </div>
    <div class="step s2">
      <span class="step-icon"><svg viewBox="0 0 20 20"><rect x="2" y="2" width="7" height="6" rx="1" fill="none" stroke="#a57a3a" stroke-width="1.3"/><rect x="11" y="2" width="7" height="6" rx="1" fill="none" stroke="#a57a3a" stroke-width="1.3"/><circle cx="6" cy="12" r="2" fill="none" stroke="#a57a3a" stroke-width="1.3"/><circle cx="14" cy="12" r="2" fill="none" stroke="#a57a3a" stroke-width="1.3"/><path d="M2 18a4 3 0 0 1 8 0M10 18a4 3 0 0 1 8 0" fill="none" stroke="#a57a3a" stroke-width="1.3"/></svg></span>
      <h3>QUESTIONS, ANSWERS AND FACTS</h3>
      <p>We will answer any questions you have and ask you enough questions to make sure we know what your goals are.<br>We will also inform you about market trends and other information related to downsizing</p>
    </div>
    <div class="step s3">
      <span class="step-icon"><svg viewBox="0 0 20 20"><path d="M3 17L15 5M17 17L5 5" stroke="#a57a3a" stroke-width="1.6"/><circle cx="15.5" cy="4.5" r="2.2" fill="#a57a3a"/><circle cx="4.5" cy="4.5" r="2.2" fill="#a57a3a"/></svg></span>
      <h3>THE TOUR AND THE TREASURE HUNT</h3>
      <p>You will take us on a tour of your home and point out items you are selling. We will take pictures, notes and point out any treasures that you may not realize you have.</p>
    </div>
    <div class="step s4">
      <span class="step-icon"><svg viewBox="0 0 20 20"><rect x="3" y="3" width="14" height="14" rx="1" fill="none" stroke="#a57a3a" stroke-width="1.4"/><circle cx="9" cy="10" r="3.2" fill="none" stroke="#a57a3a" stroke-width="1.4"/><path d="M11.4 12.4L15 16" stroke="#a57a3a" stroke-width="1.6"/></svg></span>
      <h3>RESEARCH, RESEARCH, RESEARCH</h3>
      <p>We take our notes and photographs back to research your items. Then we will check with our network of experts, dealers and buyers across the country to determine the best market.</p>
    </div>
    <div class="step s5">
      <span class="step-icon"><svg viewBox="0 0 20 20"><rect x="2" y="3" width="8" height="7" fill="#a57a3a"/><rect x="11" y="10" width="7" height="8" fill="none" stroke="#a57a3a" stroke-width="1.4"/><path d="M4 18h5M6.5 12v6M14 3v5" stroke="#a57a3a" stroke-width="1.4"/></svg></span>
      <h3>THE GAME PLAN</h3>
      <p>We will go over our findings with you. Then we will discuss ways to sell the items to get the highest return.</p>
    </div>

    <div class="abs asset-box">A collectible asset is any item or group of items owned by an individual, entity or group. The value of each item is based on rarity, condition and demand. Common categories of collectibles include antiques, jewelry, watches, art, toys, coins, wine &amp; spirits, sports memorabilia, militaria, historical documents, comic books and fashion. The list goes on.</div>
    <div class="tab asset-tab">WHAT IS A COLLECTIBLE ASSET</div>

    <figure class="item-photo i1" role="img" aria-label="Photo of a jeweled harlequin figurine brooch"><div></div></figure>
    <figure class="item-photo i2" role="img" aria-label="Photo of a set of collectible coins in a case"><div></div></figure>
    <figure class="item-photo i3" role="img" aria-label="Photo of an antique sterling silver compote"><div></div></figure>
    <figure class="item-photo i4" role="img" aria-label="Photo of a carved rock crystal snuff bottle"><div></div></figure>

    <footer class="abs footer">
      <span class="contact"><svg viewBox="0 0 10 10"><circle cx="5" cy="5" r="5" fill="#c19a5b"/><circle cx="5" cy="4" r="1.8" fill="#1f120c"/><path d="M2 8.5a3 2.4 0 0 1 6 0z" fill="#1f120c"/></svg>Walter Brannock</span>
      <span class="contact"><svg viewBox="0 0 10 10"><path d="M2 1l2 2-1 1.2a6 6 0 0 0 2.8 2.8L7 6l2 2-1.3 1.3C4.5 9 1 5.5.7 2.3z" fill="#c19a5b"/></svg>555-382-7190</span>
      <span class="contact"><svg viewBox="0 0 10 10"><circle cx="5" cy="5" r="5" fill="#c19a5b"/><rect x="2.2" y="3.2" width="5.6" height="3.8" fill="#1f120c"/><path d="M2.2 3.2L5 5.4 7.8 3.2" stroke="#c19a5b" stroke-width=".6" fill="none"/></svg>info@walterbbrannock-example.com</span>
      <span class="contact"><svg viewBox="0 0 10 10"><circle cx="5" cy="5" r="4.4" fill="none" stroke="#c19a5b" stroke-width="1.2"/><path d="M.6 5h8.8M5 .6c-2.4 2.6-2.4 6.2 0 8.8M5 .6c2.4 2.6 2.4 6.2 0 8.8" stroke="#c19a5b" stroke-width=".7" fill="none"/></svg>www.walterbbrannock-example.com</span>
    </footer>
  </section>
</body>
</html>
```